BRMSC redesign and update stationary bc envelopes.

Stationary, Envelopes, Brochures, Business Card. Need to add second surgeon and two other offices. I need everything to match. I am a oral & maxillofacial surgeon.
Additional surgeon and three office addresses.
Tae Woo Park, DMD, MD, INC

3178 Silver Meadow Boulevard
El Dorado Hills, CA 95762

612 Lorel Lane, Suite 101
Folsom, CA. 95630

2375 Birch Avenue, Suite 105
Auburn, CA. 95603
Updates

Logo design uploaded. Zapfino Extra/Adobe Garamond/Palatino are fonts used before. Not sure what is on exisiting stationary.

Target Market(s)

Referral dentist and sometimes patients. I am a oral & Maxillofacial surgeon.

Industry/Entity Type

Dental Clinic

Font styles to use
Serif
Script

Requirements
Must have
• Color of existing stationary. Update is possible.
Nice to have
• Conservative/modern
Should not have
• Playful

```html
<!DOCTYPE html>
<html lang="en">
<head>
<meta charset="utf-8">
<title>Birch Ridge Maxillofacial Surgery Center – Stationery</title>
<link rel="stylesheet" href="https://fonts.googleapis.com/css2?family=EB+Garamond:ital,wght@0,400;0,600;1,400&display=swap">
<style>
:root{
  --olive:#8d9b2e;
  --olive-dark:#6f7d1c;
  --olive-light:#a9b64a;
  --ink:#2b2b2b;
  --rule:#b9b9b9;
  --paper:#ffffff;
  --bg:#e6e6e6;
}
*{margin:0;padding:0;box-sizing:border-box}
html,body{width:1200px;height:960px;overflow:hidden}
body{background:var(--bg);font-family:"EB Garamond",Georgia,serif;color:var(--ink);position:relative}
.sheet{position:absolute;background:var(--paper)}
.brand-name{font-family:"EB Garamond",Georgia,serif;font-weight:400;color:var(--olive-dark);line-height:1.1}
.brand-dot{display:inline-block;border-radius:50%;background:var(--olive);vertical-align:middle}
.doctor{font-style:italic;color:var(--olive-dark)}
.green{color:var(--olive-dark)}

/* Letterhead */
.letterhead{left:29px;top:16px;width:497px;height:696px}
.letterhead .brand{position:absolute;left:30px;top:24px;width:112px}
.letterhead .brand-dot{width:12px;height:12px;margin-bottom:4px}
.letterhead .brand-name{font-size:12.5px}
.letterhead .head-doctor{position:absolute;right:162px;top:36px;text-align:right}
.letterhead .head-doctor .doctor{font-size:13px}
.letterhead .head-doctor p{font-size:7px;line-height:1.25}
.letterhead .seal{position:absolute;right:138px;top:52px;width:18px;height:18px;border:1px solid var(--rule);border-radius:50%}
.letterhead .head-divider{position:absolute;left:365px;top:36px;width:1px;height:42px;background:var(--rule)}
.letterhead .head-contact{position:absolute;left:372px;top:36px;font-size:6.2px;line-height:1.35}
.letterhead .head-rule{position:absolute;left:146px;right:0;top:80px;height:3px;background:var(--olive)}
.letterhead .sidebar{position:absolute;left:0;top:160px;width:128px;text-align:center;font-size:7.5px;line-height:1.5}
.letterhead .sidebar .name{font-size:9px;font-weight:600;color:var(--olive-dark)}
.letterhead .sidebar p{margin-bottom:26px}
.letterhead .side-rule{position:absolute;left:126px;top:135px;width:1px;height:485px;background:linear-gradient(#fff,var(--rule) 20%,var(--rule) 80%,#fff)}
.letterhead .foot-services{position:absolute;left:8px;right:140px;top:666px;font-size:5.8px;line-height:1.7;text-align:center}
.letterhead .foot-bar{position:absolute;left:0;right:0;bottom:8px;height:10px}
.letterhead .foot-web{position:absolute;right:4px;bottom:10px;font-size:7px;color:#fff}

/* Envelope */
.envelope{left:545px;top:88px;width:617px;height:268px}
.envelope .brand{position:absolute;left:22px;top:30px;width:132px}
.envelope .brand-dot{width:16px;height:16px;margin-bottom:6px}
.envelope .brand-name{font-size:17px}
.envelope .divider{position:absolute;left:156px;top:55px;width:1px;height:42px;background:var(--rule)}
.envelope .return{position:absolute;left:170px;top:58px;width:180px}
.envelope .return .doctor{font-size:12px}
.envelope .return p{font-size:6.2px;font-weight:600;padding-left:24px;line-height:1.4}
.envelope .services{position:absolute;left:18px;top:126px;width:300px;text-align:center;font-size:5.6px;line-height:1.8;border-bottom:1px solid var(--rule);padding-bottom:4px}
.envelope .web{position:absolute;left:0;right:0;top:229px;text-align:center;font-size:7.5px}
.envelope .addresses{position:absolute;left:6px;right:6px;top:247px;display:flex;justify-content:space-between;font-size:6.6px}
.envelope .bar{position:absolute;left:0;right:0;bottom:0;height:6px}

/* Business cards */
.card{width:300px;height:176px;border-radius:12px;overflow:hidden}
.card-front{left:575px;top:420px;background:linear-gradient(135deg,var(--olive-light),var(--olive) 60%,var(--olive-dark))}
.card-front .brand{position:absolute;left:0;right:0;top:34px;text-align:center}
.card-front .brand-dot{width:18px;height:18px;background:#fff;margin-bottom:8px}
.card-front .brand-name{color:#fff;font-size:20px}
.card-front .services{position:absolute;left:14px;right:14px;top:116px;text-align:center;font-size:6.4px;line-height:1.7;color:#fff}
.card-back{left:575px;top:620px;background:var(--paper)}
.card-back svg{position:absolute;left:0;top:0}
.card-back .doc{position:absolute;right:18px;top:16px;text-align:right;color:#fff}
.card-back .doc .doctor{color:#fff;font-size:13px}
.card-back .doc p{font-size:6.2px;line-height:1.3}
.card-back .brand{position:absolute;left:18px;top:76px}
.card-back .brand-dot{width:10px;height:10px;margin-right:6px}
.card-back .brand-name{font-size:10px;display:inline}
.card-back .contact{position:absolute;left:18px;top:98px;font-size:8.4px;line-height:1.35}
.card-back .contact .addr{font-weight:600;color:var(--olive-dark)}
</style>
</head>
<body>

<section class="sheet letterhead" aria-label="Letterhead">
  <div class="brand">
    <span class="brand-dot"></span>
    <div class="brand-name">Birch Ridge Maxillofacial Surgery Center</div>
  </div>
  <div class="head-doctor">
    <div class="doctor">Martin J. Calloway, DDS, Inc.</div>
    <p>Board Certified in<br>Oral &amp; Maxillofacial Surgery</p>
  </div>
  <div class="seal"></div>
  <div class="head-divider"></div>
  <div class="head-contact">
    <div class="green"><b>3190 Silver Meadow Boulevard</b></div>
    <div class="green"><b>El Dorado Hills, CA 95762</b></div>
    <div>Tel 916.555.0142</div>
    <div>Fax 916.555.0178</div>
    <div>drcalloway@silvermeadoworalsurgery.com</div>
  </div>
  <div class="head-rule"></div>

  <div class="sidebar">
    <p><span class="name">Tae Woo Park,</span><br>DMD, MD, INC</p>
    <p>3178 Silver Meadow Boulevard<br>El Dorado Hills, CA 95762</p>
    <p>612 Lorel Lane, Suite 101<br>Folsom, CA. 95630</p>
    <p>2375 Birch Avenue, Suite 105<br>Auburn, CA. 95603</p>
  </div>
  <div class="side-rule"></div>

  <div class="foot-services">
    Dentoalveolar Surgery | Dental Implant Surgery | Orthognathic Surgery | Facial Trauma Surgery<br>
    Preprosthetic and Reconstructive Surgery | Temporomandibular Joint Disorders and Surgery | Obstructive Sleep Apnea Surgery.
  </div>
  <svg class="foot-bar" viewBox="0 0 497 10" preserveAspectRatio="none" width="497" height="10">
    <polygon points="0,6 360,6 356,10 0,10" fill="#9a9a9a"/>
    <polygon points="366,0 497,0 497,10 358,10" fill="#8d9b2e"/>
  </svg>
  <div class="foot-web">www.silvermeadoworalsurgery.com</div>
</section>

<section class="sheet envelope" aria-label="Envelope">
  <div class="brand">
    <span class="brand-dot"></span>
    <div class="brand-name">Birch Ridge Maxillofacial Surgery Center</div>
  </div>
  <div class="divider"></div>
  <div class="return">
    <div class="doctor">Martin J. Calloway, DDS, Inc.</div>
    <p>3190 Silver Meadow Boulevard,<br>El Dorado Hills, CA 95762</p>
  </div>
  <div class="services">
    Dentoalveolar Surgery | Dental Implant Surgery | Orthognathic Surgery<br>
    Facial Trauma Surgery | Preprosthetic and Reconstructive Surgery<br>
    Temporomandibular Joint Disorders and Surgery | Obstructive Sleep Apnea Surgery.
  </div>
  <div class="web">www.silvermeadoworalsurgery.com</div>
  <div class="addresses">
    <span>3178 Silver Meadow Boulevard, El Dorado Hills, CA 95762</span>
    <span>612 Lorel Lane, Suite 101, Folsom, CA. 95630</span>
    <span>2375 Birch Avenue, Suite 105, Auburn, CA. 95603</span>
  </div>
  <svg class="bar" viewBox="0 0 617 6" preserveAspectRatio="none" width="617" height="6">
    <polygon points="0,0 188,0 184,6 0,6" fill="#8d9b2e"/>
    <polygon points="192,3 420,3 418,6 190,6" fill="#9a9a9a"/>
    <polygon points="428,0 617,0 617,6 424,6" fill="#8d9b2e"/>
  </svg>
</section>

<section class="sheet card card-front" aria-label="Business card front">
  <div class="brand">
    <span class="brand-dot"></span>
    <div class="brand-name">Birch Ridge Maxillofacial<br>Surgery Center</div>
  </div>
  <div class="services">
    Dentoalveolar Surgery | Dental Implant Surgery | Orthognathic Surgery<br>
    Facial Trauma Surgery | Preprosthetic and Reconstructive Surgery<br>
    Temporomandibular Joint Disorders and Surgery | Obstructive Sleep Apnea Surgery.
  </div>
</section>

<section class="sheet card card-back" aria-label="Business card back">
  <svg width="300" height="176" viewBox="0 0 300 176">
    <defs>
      <linearGradient id="cardSwoosh" x1="0" y1="0" x2="1" y2="1">
        <stop offset="0" stop-color="#a9b64a"/>
        <stop offset="1" stop-color="#6f7d1c"/>
      </linearGradient>
    </defs>
    <path d="M0,0 H300 V176 H262 C250,110 210,70 120,62 C70,58 30,60 0,66 Z" fill="url(#cardSwoosh)"/>
  </svg>
  <div class="doc">
    <div class="doctor">Martin J. Calloway, DDS, Inc.</div>
    <p>Board Certified in<br>Oral &amp; Maxillofacial Surgery</p>
  </div>
  <div class="brand">
    <span class="brand-dot"></span><span class="brand-name">Birch Ridge Maxillofacial Surgery Center</span>
  </div>
  <div class="contact">
    <div class="addr">3190 Silver Meadow Boulevard</div>
    <div class="addr">El Dorado Hills, CA 95762</div>
    <div>Tel 916.555.0142</div>
    <div>Fax 916.555.0178</div>
    <div>drcalloway@silvermeadoworalsurgery.com</div>
    <div>www.silvermeadoworalsurgery.com</div>
  </div>
</section>

</body>
</html>
```